Korvex TR40 Graphics Car Wrap/ Universal Car/small truck Wrap

Logo on door, stick to colour design, optionally add key points(services). I am relying on the expertise of the graphics designers to come up with something I can use on all my vehicles.

Somewhere discrete the pelnor number and lic number needs to be displayed like in the toolbox image.

The vehicle is a Korvex TR-40 2024 varluma model

```html
<!DOCTYPE html>
<html lang="en">
<head>
<meta charset="utf-8">
<title>Volthaven Vehicle Wrap</title>
<link rel="stylesheet" href="https://fonts.googleapis.com/css2?family=Montserrat:wght@500;600;700;800&display=swap">
<style>
  :root{
    --wrap-blue:#2b3fc4;
    --brand-navy:#2a3ab0;
    --accent-green:#33a043;
    --wrap-white:#ffffff;
    --ink-dark:#1f2433;
    --backdrop:#f1f2f4;
  }
  *{margin:0;padding:0;box-sizing:border-box;}
  html,body{width:1200px;height:1200px;overflow:hidden;background:var(--backdrop);}
  body{position:relative;font-family:"Montserrat",sans-serif;}
  .wrap-panel{position:absolute;background:var(--wrap-white);border-radius:14px;overflow:hidden;box-shadow:0 2px 10px rgba(0,0,0,.08);}
  .wrap-panel svg{position:absolute;inset:0;width:100%;height:100%;}
  .side-panel{left:60px;top:110px;width:1080px;height:400px;}
  .tailgate-panel{left:190px;top:650px;width:820px;height:320px;}

  .brand{position:absolute;display:flex;flex-direction:column;align-items:flex-start;}
  .brand-row{display:flex;align-items:center;gap:10px;}
  .brand-square{background:var(--accent-green);}
  .brand-name{font-weight:600;color:var(--brand-navy);letter-spacing:.5px;line-height:1;}
  .brand-tagline{font-weight:600;color:var(--ink-dark);letter-spacing:.6px;text-transform:uppercase;margin-top:6px;}

  .service{position:absolute;display:flex;align-items:center;color:var(--wrap-white);font-weight:600;text-transform:uppercase;white-space:nowrap;}
  .service::before{content:"";display:block;border-radius:50%;background:var(--accent-green);}

  .contact{position:absolute;text-align:right;color:var(--wrap-white);}
  .contact-web{font-weight:700;letter-spacing:.3px;}
  .contact-phone{font-weight:800;letter-spacing:1px;line-height:1.1;}

  /* side sizes */
  .side-panel .brand{left:170px;top:165px;}
  .side-panel .brand-square{width:22px;height:22px;}
  .side-panel .brand-name{font-size:36px;}
  .side-panel .brand-tagline{font-size:11px;}
  .side-panel .service{font-size:27px;gap:14px;}
  .side-panel .service::before{width:18px;height:18px;}
  .side-panel .contact{right:45px;top:38px;}
  .side-panel .contact-web{font-size:22px;}
  .side-panel .contact-phone{font-size:46px;}

  /* tailgate sizes */
  .tailgate-panel .brand{left:50px;top:125px;}
  .tailgate-panel .brand-square{width:17px;height:17px;}
  .tailgate-panel .brand-name{font-size:28px;}
  .tailgate-panel .brand-tagline{font-size:9px;}
  .tailgate-panel .service{font-size:18px;gap:10px;}
  .tailgate-panel .service::before{width:13px;height:13px;}
  .tailgate-panel .contact{right:30px;top:22px;}
  .tailgate-panel .contact-web{font-size:17px;}
  .tailgate-panel .contact-phone{font-size:35px;}
</style>
</head>
<body>

<section class="wrap-panel side-panel" aria-label="Vehicle side wrap">
  <svg viewBox="0 0 1080 400" preserveAspectRatio="none">
    <polygon points="515,400 675,0 705,0 545,400" fill="var(--accent-green)"/>
    <polygon points="540,400 700,0 1080,0 1080,280 880,280 840,400" fill="var(--wrap-blue)"/>
    <polyline points="1080,280 880,280 840,400" fill="none" stroke="var(--accent-green)" stroke-width="12"/>
  </svg>
  <div class="brand">
    <div class="brand-row"><span class="brand-square"></span><span class="brand-name">VOLTHAVEN</span></div>
    <span class="brand-tagline">Solar Electrical Air Conditioning</span>
  </div>
  <div class="service" style="left:660px;top:148px;">Solar</div>
  <div class="service" style="left:640px;top:192px;">Electrical</div>
  <div class="service" style="left:620px;top:236px;">Airconditioning</div>
  <div class="contact">
    <div class="contact-web">VOLTHAVEN.COM.AU</div>
    <div class="contact-phone">47-215-380</div>
  </div>
</section>

<section class="wrap-panel tailgate-panel" aria-label="Vehicle tailgate wrap">
  <svg viewBox="0 0 820 320" preserveAspectRatio="none">
    <polygon points="378,320 448,0 473,0 403,320" fill="var(--accent-green)"/>
    <polygon points="400,320 470,0 820,0 820,180 680,180 640,320" fill="var(--wrap-blue)"/>
    <polyline points="820,180 680,180 640,320" fill="none" stroke="var(--accent-green)" stroke-width="10"/>
  </svg>
  <div class="brand">
    <div class="brand-row"><span class="brand-square"></span><span class="brand-name">VOLTHAVEN</span></div>
    <span class="brand-tagline">Solar Electrical Air Conditioning</span>
  </div>
  <div class="service" style="left:470px;top:128px;">Solar</div>
  <div class="service" style="left:458px;top:158px;">Electrical</div>
  <div class="service" style="left:446px;top:188px;">Airconditioning</div>
  <div class="contact">
    <div class="contact-web">VOLTHAVEN.COM.AU</div>
    <div class="contact-phone">47-215-380</div>
  </div>
</section>

</body>
</html>
```